Business Card Design

Im a small business that specialises in all aspects of sign installation, big and small, domestic and commercial. I have a construction and carpentry background. I'm after a professional looking business card, that has my logo as the forefront of the card incorporating the same colours as the my logo. No slogan as yet, but open to suggestions. The final design should communicate quality and class workmanship.

Target Market(s)

Managers and Owners of businesses

Industry/Entity Type

Small Business

Contact Information for Business Card

Carwyn Solbeck
Mob: 0417295036
Email: kto.fitouts@quillmail.net

Sign Installation
Property Improvement and Maintenance
Trade Services

Colors
dbdbdb
000000
ffffff

Requirements
Must have
• Logo
My name
My contact details
What I specialise in
Nice to have
• background image/images that are only just noticeable and do not take away from the logo or text.
Should not have
• No colours that contrast from my logo
No heavy machinery images to be used
Logo must stand out

```html
<!DOCTYPE html>
<html lang="en">
<head>
<meta charset="utf-8">
<title>KTO Installations – Business Card</title>
<link rel="stylesheet" href="https://fonts.googleapis.com/css2?family=Montserrat:wght@600;700&family=Ubuntu:wght@400;500&display=swap">
<style>
  :root {
    --bg: #dbdbdb;
    --card: #ffffff;
    --ink: #1f1f1f;
    --black: #222222;
    --blue: #2b4fa3;
    --photo-sky: #c9d3ec;
    --photo-wall: #d8d6d4;
    --photo-accent: #e9c7a6;
  }
  * { box-sizing: border-box; margin: 0; padding: 0; }
  html, body { width: 1200px; height: 800px; overflow: hidden; }
  body {
    background: var(--bg);
    display: flex;
    align-items: center;
    justify-content: center;
    gap: 50px;
    font-family: "Ubuntu", sans-serif;
  }
  .card {
    position: relative;
    width: 540px;
    height: 310px;
    background: var(--card);
    overflow: hidden;
    box-shadow: 0 6px 18px rgba(0,0,0,0.18);
  }
  /* Back */
  .card-back__photo {
    position: absolute; inset: 0;
    background:
      linear-gradient(115deg, transparent 40%, var(--photo-accent) 48%, transparent 56%),
      linear-gradient(160deg, var(--photo-sky) 0%, var(--photo-sky) 45%, var(--photo-wall) 46%, var(--photo-wall) 100%);
    opacity: 0.85;
  }
  .brand {
    display: flex; align-items: center; gap: 12px;
    font-family: "Montserrat", sans-serif;
    font-weight: 700;
    color: var(--blue);
    letter-spacing: 0.06em;
    white-space: nowrap;
  }
  .brand__dot {
    border: 5px solid var(--blue);
    border-radius: 50%;
    flex: none;
  }
  .card-back .brand {
    position: absolute; left: 50%; top: 50%;
    transform: translate(-50%, -50%);
    font-size: 30px;
  }
  .card-back .brand__dot { width: 62px; height: 62px; }
  /* Front */
  .card-front__swoosh { position: absolute; inset: 0; }
  .identity { position: absolute; left: 36px; top: 46px; }
  .identity__name {
    font-family: "Montserrat", sans-serif;
    font-weight: 700;
    font-size: 21px;
    letter-spacing: 0.08em;
    color: var(--ink);
    text-transform: uppercase;
  }
  .identity__role {
    font-family: "Montserrat", sans-serif;
    font-weight: 600;
    font-size: 16px;
    color: var(--blue);
    margin-top: 2px;
  }
  .services {
    position: absolute; left: 36px; top: 140px;
    font-size: 13.5px; font-weight: 500;
    color: var(--blue); line-height: 1.35;
  }
  .contact {
    position: absolute; left: 36px; top: 192px;
    font-size: 13.5px; color: var(--ink); line-height: 1.45;
  }
  .contact__label { color: var(--blue); font-weight: 500; }
  .card-front .brand {
    position: absolute; right: 26px; top: 108px;
    font-size: 17px; gap: 9px;
  }
  .card-front .brand__dot { width: 40px; height: 40px; border-width: 4px; }
</style>
</head>
<body>
  <section class="card card-back" aria-label="Business card back">
    <div class="card-back__photo" role="img" aria-label="Faint background photo of a sign installation on a building facade"></div>
    <div class="brand"><span class="brand__dot"></span>KTO INSTALLATIONS</div>
  </section>

  <section class="card card-front" aria-label="Business card front">
    <svg class="card-front__swoosh" width="540" height="310" viewBox="0 0 540 310" aria-hidden="true">
      <path d="M0,276 Q300,268 540,158 L540,310 L0,310 Z" fill="var(--blue)"/>
      <path d="M0,286 Q305,278 540,172 L540,310 L0,310 Z" fill="var(--black)"/>
    </svg>
    <div class="identity">
      <h1 class="identity__name">Carwyn Solbeck</h1>
      <p class="identity__role">Company Position</p>
    </div>
    <p class="services">Sign Installation Property Improvement<br>and Maintenance Trade Services</p>
    <p class="contact">
      <span class="contact__label">E:</span> kto.fitouts@quillmail.net<br>
      <span class="contact__label">F:</span> 041 729 5036
    </p>
    <div class="brand"><span class="brand__dot"></span>KTO INSTALLATIONS</div>
  </section>
</body>
</html>
```